Store Front Sign for Vape Store

Interested in getting a store front sign graphic done. Sign is for over the door (lighted sign). Dimensions of sign: 6 feet long x 2 feet high.
Sign is for a Vape Store. I have attached the logo to be used.
Looking for a modern and professional look
Phone numbers to be used.
Whatsapp# 364-9105
Contact #519-7036
Sign should have Instagram & Facebook logos and. handle @lagoonmistco

Industry/Entity Type

Vape | Electronic Cigarettes

Colors

Designer to choose colors to be used in the design.

Requirements
Must have
• Facebook and Instagram Logos. Contact Numbers.
Should not have
• Any Persons.

```html
<!DOCTYPE html>
<html lang="en">
<head>
<meta charset="utf-8">
<title>Lagoon Mist – Storefront Sign</title>
<link rel="stylesheet" href="https://fonts.googleapis.com/css2?family=Arimo:wght@400;700&display=swap">
<style>
  :root {
    --sign-white: #ffffff;
    --sign-black: #000000;
    --sign-charcoal: #3a3a3a;
    --accent-blue: #1aa3e0;
    --badge-dark: #2b2b2b;
    --badge-ring: #0f7fc0;
    --text-light: #ffffff;
  }
  html, body {
    margin: 0;
    padding: 0;
    width: 1200px;
    height: 400px;
    overflow: hidden;
    background: var(--sign-white);
  }
  .sign {
    position: relative;
    width: 1200px;
    height: 400px;
    background: var(--sign-white);
    font-family: "Arimo", Arial, sans-serif;
    overflow: hidden;
  }
  .sign__backdrop {
    position: absolute;
    inset: 0;
  }
  .brand-badge {
    position: absolute;
    left: 66px;
    top: 24px;
    width: 286px;
    height: 286px;
    border-radius: 50%;
    background: radial-gradient(circle at 45% 40%, #4a4a4a 0%, var(--badge-dark) 70%);
    box-shadow: inset 0 0 0 6px #1c1c1c, inset 0 0 0 10px var(--badge-ring), inset 0 0 0 14px #1c1c1c;
    display: flex;
    align-items: center;
    justify-content: center;
  }
  .brand-badge__name {
    margin: 0;
    color: var(--text-light);
    font-weight: 700;
    font-size: 44px;
    line-height: 1.05;
    text-align: center;
  }
  .contact {
    position: absolute;
    color: var(--text-light);
    display: flex;
    align-items: center;
  }
  .contact--whatsapp { left: 722px; top: 140px; }
  .contact--phone    { left: 722px; top: 212px; }
  .contact__icon {
    width: 56px;
    height: 56px;
    flex: none;
    margin-right: 14px;
  }
  .contact__number {
    font-size: 61px;
    line-height: 1;
    letter-spacing: 0.5px;
  }
  .social {
    position: absolute;
    left: 688px;
    top: 308px;
    display: flex;
    align-items: center;
    color: var(--text-light);
  }
  .social__dot {
    width: 40px;
    height: 40px;
    border-radius: 50%;
    background: var(--accent-blue);
    margin-right: 5px;
  }
  .social__handle {
    margin-left: 6px;
    font-size: 37px;
    line-height: 1;
  }
</style>
</head>
<body>
<main class="sign">
  <svg class="sign__backdrop" width="1200" height="400" viewBox="0 0 1200 400" aria-hidden="true">
    <defs>
      <linearGradient id="wave-fill" x1="0" y1="0" x2="1" y2="0">
        <stop offset="0" stop-color="var(--sign-charcoal)"/>
        <stop offset="0.55" stop-color="var(--sign-black)"/>
        <stop offset="1" stop-color="var(--sign-black)"/>
      </linearGradient>
    </defs>
    <path class="wave-band" fill="url(#wave-fill)"
      d="M0,228 C80,350 300,378 500,262 C680,150 820,68 960,72 C1080,78 1160,140 1200,196 L1200,400 L0,400 Z"/>
    <path class="accent-swoosh accent-swoosh--left" fill="none" stroke="var(--accent-blue)" stroke-width="7"
      d="M0,196 C60,322 270,356 430,262"/>
    <path class="accent-swoosh accent-swoosh--right" fill="none" stroke="var(--accent-blue)" stroke-width="7"
      d="M868,66 C1000,58 1140,118 1200,186"/>
  </svg>

  <div class="brand-badge">
    <p class="brand-badge__name">Lagoon<br>Mist</p>
  </div>

  <div class="contact contact--whatsapp">
    <svg class="contact__icon" viewBox="0 0 56 56" aria-hidden="true">
      <circle cx="28" cy="28" r="28" fill="var(--accent-blue)"/>
    </svg>
    <span class="contact__number">364-9105</span>
  </div>

  <div class="contact contact--phone">
    <svg class="contact__icon" viewBox="0 0 56 56" aria-hidden="true">
      <circle cx="28" cy="28" r="28" fill="var(--accent-blue)"/>
      <path fill="var(--sign-black)"
        d="M19,14 l6,-1 l4,9 l-4,3 c2,5 5,8 9,10 l3,-4 l9,4 l-1,6 c-1,2 -3,3 -6,3 c-12,-2 -21,-11 -23,-23 c0,-3 1,-6 3,-7 z"/>
    </svg>
    <span class="contact__number">519-7036</span>
  </div>

  <div class="social">
    <span class="social__dot" aria-hidden="true"></span>
    <span class="social__dot" aria-hidden="true"></span>
    <span class="social__handle">@lagoonmistco</span>
  </div>
</main>
</body>
</html>
```